Newsletter Email Banner

Create a banner image for a newsletter template.
Incorporate 3 lines of copy:
1. Contractor Vetting Services
2. Live & Online Education
3. Safety & Compliance
Use the attached images. Use the logo layout that works best for the design.
Orange color code: RGB: R 255; G 153; B 0

Target Market(s)

Residential construction contractors

Industry/Entity Type

Construction

Font styles to use
Sans Serif

Colors
f78f20

Requirements
Must have
• High quality image file
Nice to have
• Not sure

```html
<!DOCTYPE html>
<html lang="en">
<head>
<meta charset="utf-8">
<title>Summit Builders Guild – Newsletter Banner</title>
<link rel="stylesheet" href="https://fonts.googleapis.com/css2?family=Montserrat:wght@600;800&display=swap">
<style>
  :root {
    --sky-top: #8ccaf0;
    --sky-mid: #bfe2f7;
    --sky-low: #e6f4fc;
    --ink: #2e2e30;
    --bar: #0d0d0d;
    --orange: #f78f20;
    --white: #ffffff;
    --art-tone-a: #7fa36a;
    --art-tone-b: #e7cf6a;
  }
  * { margin: 0; padding: 0; box-sizing: border-box; }
  html, body { width: 1200px; height: 600px; overflow: hidden; }
  body { font-family: "Montserrat", Arial, sans-serif; }

  .banner {
    position: relative;
    width: 1200px;
    height: 600px;
    overflow: hidden;
    background: linear-gradient(180deg, var(--sky-top) 0%, var(--sky-mid) 45%, var(--sky-low) 100%);
  }

  .brand {
    position: absolute;
    left: 74px;
    top: 88px;
    color: var(--ink);
    font-weight: 800;
    text-transform: uppercase;
    line-height: 0.92;
  }
  .brand__line { display: block; font-size: 64px; letter-spacing: -1px; }
  .brand__sub {
    display: block;
    margin-top: 14px;
    font-size: 22px;
    letter-spacing: 16px;
    padding-left: 14px;
  }

  .services {
    position: absolute;
    left: 0;
    top: 291px;
    list-style: none;
  }
  .service {
    position: relative;
    height: 60px;
    margin-bottom: 10px;
  }
  .service svg { position: absolute; left: 0; top: 0; }
  .service__label {
    position: absolute;
    left: 48px;
    top: 0;
    height: 60px;
    line-height: 60px;
    color: var(--white);
    font-weight: 600;
    font-size: 28px;
    text-transform: uppercase;
    white-space: nowrap;
  }

  .hero-art {
    position: absolute;
    left: 630px;
    top: 70px;
    width: 545px;
    height: 480px;
    background: linear-gradient(160deg, var(--art-tone-a) 0%, var(--art-tone-b) 100%);
  }
</style>
</head>
<body>
  <main class="banner">
    <div class="brand">
      <span class="brand__line">Summit</span>
      <span class="brand__line">Builders</span>
      <span class="brand__sub">Guild</span>
    </div>

    <ul class="services">
      <li class="service">
        <svg width="640" height="60" aria-hidden="true">
          <polygon points="0,0 600,0 580,60 0,60" fill="var(--bar)"/>
          <polygon points="600,0 622,0 598,60 580,60" fill="var(--orange)"/>
        </svg>
        <span class="service__label">1. Contractor Vetting Services</span>
      </li>
      <li class="service">
        <svg width="640" height="60" aria-hidden="true">
          <polygon points="0,0 520,0 500,60 0,60" fill="var(--bar)"/>
          <polygon points="520,0 542,0 518,60 500,60" fill="var(--orange)"/>
        </svg>
        <span class="service__label">2. Live &amp; Online Education</span>
      </li>
      <li class="service">
        <svg width="640" height="60" aria-hidden="true">
          <polygon points="0,0 466,0 446,60 0,60" fill="var(--bar)"/>
          <polygon points="466,0 488,0 464,60 446,60" fill="var(--orange)"/>
        </svg>
        <span class="service__label">3. Safety &amp; Compliance</span>
      </li>
    </ul>

    <div class="hero-art" role="img" aria-label="Photo of a yellow construction hard hat topped with a miniature landscape of forest, river, beach and village"></div>
  </main>
</body>
</html>
```